This project is to address Personal Life issues/ Health & Wellness using a certified Professional Coaching Approach.

Major coaching areas include: Weight loss, Overwhelm/ Time Management, Increased Energy, Leadership, Improved Relationships, Finding Your Life Purpose & passion, Self Esteem & Confidence,

The combination of a board certified Internal Medicine physician and
professional coach is a powerful and unique approach to help people achieve
better health and well being.

Target Market(s)

Existing or potentially new patients/clients interested in any of the listed categories of coaching.

Industry/Entity Type

Life Coaching

Font styles to use
Sans Serif

Colors
00a990
0292cd
0255a3
33b8a4
a64599
6b449b
876aae
3176b5
33a6d7

Requirements
Must have
• Design specifics: Use of deep blues/greens using nature imagery is
• preferred- see our website for at Brightvalecare.com
• Each category of coaching must be listed out with a paragraph of description below each- I will provide the description in an attachment that is pending.
• Title of Brochure: "Clearbrook Health Personal Life & Wellness Coaching."
• "Coaching That Works!"
Nice to have
• A definition of coaching on the front of brochure:
• " A compassionate catalyzing relationship - The art of facilitating the performance, learning and development of another so they may achieve what the want faster.”
• Also on the front please place: "Stuck? Ask about a free coaching consult with Dr. Tavren to learn more!"
Should not have
• Should not have anything in the brochure that mentions medical services from the website outside of weight loss. The purpose of the brochure is to promote the coaching services.

```html
<!DOCTYPE html>
<html lang="en">
<head>
<meta charset="utf-8">
<title>Clearbrook Health Personal Life &amp; Wellness Coaching Brochure</title>
<link href="https://fonts.googleapis.com/css2?family=Open+Sans:wght@400;600;700&family=Tinos:wght@400;700&display=swap" rel="stylesheet">
<style>
:root{
  --navy:#2e3192;
  --green:#1e9a4a;
  --ink:#444;
  --slate:#5a5a5a;
  --paper:#fff;
  --bg:#dcdcdc;
}
*{box-sizing:border-box;margin:0;padding:0}
html,body{width:1200px;height:1200px;overflow:hidden;background:var(--bg);font-family:"Open Sans",sans-serif;color:var(--ink)}
.sheet{position:absolute;left:80px;width:1040px;background:var(--paper);display:flex;box-shadow:0 8px 24px rgba(0,0,0,.18)}
.sheet--outside{top:36px;height:540px}
.sheet--inside{top:620px;height:550px}
.panel{position:relative;width:346.67px;height:100%;overflow:hidden}
p{font-size:8.6px;line-height:1.45}
.brand{display:flex;align-items:center;gap:6px;font-family:"Tinos",serif;font-size:11px;color:var(--navy);letter-spacing:.5px;white-space:nowrap}
.brand .dot{width:12px;height:12px;border-radius:50%;background:var(--navy);flex:0 0 12px}

/* outside panel 1 */
.intro{padding:28px 24px 0}
.intro h2{font-family:"Tinos",serif;color:var(--navy);font-size:17px;font-weight:700;margin-bottom:8px}
.intro .definition{font-style:italic;margin-bottom:6px}
.intro .lead{font-weight:700;font-size:9px;margin:8px 0 10px}
.areas{display:grid;grid-template-columns:1fr 1fr;margin:0 24px}
.area{height:102px;padding:9px 10px}
.area h4{font-size:9.5px;margin-bottom:4px}
.area p{font-size:7.4px;line-height:1.35}
.area--green{background:var(--green);color:#fff}
.area--navy{background:var(--navy);color:#fff}
.area--plain{background:#fff}
.area--brand{display:flex;align-items:center;justify-content:center}
.area--brand .brand{font-size:10px}

/* outside panel 2 */
.about{background:var(--navy);color:#fff;padding:30px 28px}
.about h3{font-family:"Tinos",serif;font-size:16px;letter-spacing:1px;margin-bottom:10px}
.about p{font-size:8.8px;margin-bottom:8px}
.about hr{border:0;border-top:1px solid rgba(255,255,255,.6);margin:18px 0}
.about .brand{color:#fff;margin-bottom:18px}
.about .brand .dot{background:#fff}
.contact h4{font-family:"Tinos",serif;font-size:17px;margin-bottom:12px}
.contact li{list-style:none;display:flex;gap:9px;font-family:"Tinos",serif;font-size:14px;margin-bottom:10px;align-items:flex-start}
.contact svg{flex:0 0 14px;margin-top:3px}

/* outside panel 3 */
.cover .brand{position:absolute;top:22px;right:22px}
.cover .photo{position:absolute;left:30px;right:0;top:60px;height:250px;background:radial-gradient(ellipse at 65% 50%,#e6b3b0 0,transparent 45%),linear-gradient(135deg,#e9edf2,#cfd6df 55%,#9fb4cc)}
.cover .titleband{position:absolute;left:30px;right:0;top:300px;height:150px;background:var(--navy);color:#fff;display:flex;flex-direction:column;align-items:center;justify-content:center;text-align:center;padding:0 14px}
.cover .titleband h1{font-family:"Tinos",serif;font-weight:400;font-size:21px;line-height:1.1;letter-spacing:1px}
.cover .titleband .tagline{font-family:"Tinos",serif;font-size:14px;margin-top:10px;font-weight:700}
.cover .url{position:absolute;left:50px;top:466px;background:var(--green);color:#fff;font-weight:700;font-size:12px;padding:5px 18px}
.cover .consult{position:absolute;left:50px;right:24px;top:500px;font-size:8.6px;font-weight:600;color:var(--navy)}

/* inside */
.scene{position:absolute;left:0;right:0}
.notchband{position:absolute;left:0;right:0;height:24px}
.notchband svg{position:absolute;left:0;top:0}
.copy{position:absolute;left:26px;right:26px}
.copy h2{font-family:"Tinos",serif;color:var(--navy);font-weight:400;font-size:22px;margin-bottom:6px}
.copy h5{font-size:10px;font-weight:700;color:#333;margin:8px 0 3px;text-transform:uppercase}
.copy hr{border:0;border-top:1px solid #aaa;margin:10px 0 0;width:70%}

.life .scene{top:0;height:230px;background:linear-gradient(180deg,#c83a1a 0%,#f08a1e 35%,#5a7a3a 60%,#3d3f9a 100%)}
.life .copy{top:262px}
.purpose .copy{top:22px}
.purpose .scene{top:345px;height:205px;background:linear-gradient(90deg,#efe9e2,#f3d6cf 55%,#dfe3ea)}
.purpose .darkband{position:absolute;left:0;right:0;top:330px;height:16px;background:var(--slate)}
.wellness .scene{top:0;height:245px;background:linear-gradient(180deg,#8a6a44 0%,#6aa3d8 30%,#5f8f3e 65%,#4a7a50 100%)}
.wellness .copy{top:272px}
</style>
</head>
<body>

<section class="sheet sheet--outside">
  <div class="panel">
    <div class="intro">
      <h2>What Is Coaching?</h2>
      <p class="definition">"A compassionate catalyzing relationship - the art of facilitating the performance, learning and development of another so they may achieve what they want faster."</p>
      <p>Clearbrook Health pairs a board certified Internal Medicine physician with a certified professional coach. This unique combination helps you set clear goals, build lasting habits and move past what has kept you stuck.</p>
      <p class="lead">Our coaching focuses on five key areas:</p>
    </div>
    <div class="areas">
      <div class="area area--green"><h4>Weight Loss:</h4><p>Practical, medically informed support to reach a healthy weight and keep it, with a plan built around your life.</p></div>
      <div class="area area--plain"><h4>Energy &amp; Fitness:</h4><p>Find routines that restore your energy and make movement a natural part of each day.</p></div>
      <div class="area area--plain"><h4>Overwhelm &amp; Time</h4><p>Learn to set priorities, manage your time and lead with calm focus at work and at home.</p></div>
      <div class="area area--navy"><h4>Relationships</h4><p>Build stronger connections through clearer communication, healthy boundaries and trust.</p></div>
      <div class="area area--green"><h4>Purpose &amp; Confidence</h4><p>Discover your passion, grow your self esteem and live with direction.</p></div>
      <div class="area area--brand"><div class="brand"><span class="dot"></span>Clearbrook Health</div></div>
    </div>
  </div>

  <div class="panel about">
    <h3>ABOUT US</h3>
    <p>Clearbrook Health offers personal life and wellness coaching led by Dr. Tavren, a board certified physician and certified professional coach. Each client receives a personal, compassionate approach that turns good intentions into real results.</p>
    <p>Our goal is to help you achieve better health and well being so you may enjoy a life of quality and purpose. Whether you want to lose weight, find more energy, improve relationships or discover your life purpose, coaching gives you the clarity, support and accountability to get there faster. Contact our office to schedule a free coaching consult and see if coaching is the right fit for you.</p>
    <hr>
    <div class="brand"><span class="dot"></span>Clearbrook Health MD</div>
    <div class="contact">
      <h4>Contact Details-</h4>
      <ul>
        <li><svg width="14" height="14" viewBox="0 0 14 14"><circle cx="7" cy="7" r="7" fill="#fff"/><path d="M4.5 3.5l1.5 0 .6 2-1 .8a5 5 0 0 0 2.2 2.2l.8-1 2 .6v1.5c-3.5.3-6.4-2.6-6.1-6.1z" fill="#2e3192"/></svg>555.014.2288</li>
        <li><svg width="14" height="14" viewBox="0 0 14 14"><circle cx="7" cy="7" r="7" fill="#fff"/><path d="M7 3a2.6 2.6 0 0 0-2.6 2.6C4.4 8 7 11 7 11s2.6-3 2.6-5.4A2.6 2.6 0 0 0 7 3z" fill="#2e3192"/><circle cx="7" cy="5.6" r="1" fill="#fff"/></svg>820 LINDEN AVE.<br>MARROW FALLS, TX 78000</li>
        <li><svg width="14" height="14" viewBox="0 0 14 14"><circle cx="7" cy="7" r="7" fill="#fff"/><circle cx="7" cy="7" r="3.8" fill="none" stroke="#2e3192"/><path d="M3.2 7h7.6M7 3.2v7.6" stroke="#2e3192"/></svg>www.brightvalecare.com</li>
        <li><svg width="14" height="14" viewBox="0 0 14 14"><circle cx="7" cy="7" r="7" fill="#fff"/><rect x="3.5" y="4.5" width="7" height="5" fill="none" stroke="#2e3192"/><path d="M3.5 4.5l3.5 3 3.5-3" fill="none" stroke="#2e3192"/></svg>office.tavren@brightvalecare.com</li>
      </ul>
    </div>
  </div>

  <div class="panel cover">
    <div class="brand"><span class="dot"></span>Clearbrook Health MD</div>
    <div class="photo" role="img" aria-label="Photo of a physician in a white coat with stethoscope holding a red heart"></div>
    <div class="titleband">
      <h1>CLEARBROOK HEALTH<br>PERSONAL LIFE &amp;<br>WELLNESS COACHING</h1>
      <div class="tagline">Coaching That Works!</div>
    </div>
    <div class="url">www.brightvalecare.com</div>
    <p class="consult">Stuck? Ask about a free coaching consult with Dr. Tavren to learn more!</p>
  </div>
</section>

<section class="sheet sheet--inside">
  <div class="panel life">
    <div class="scene" role="img" aria-label="Photo of a sunset over a field of bluebonnet wildflowers"></div>
    <div class="notchband" style="top:214px">
      <svg width="347" height="40" viewBox="0 0 347 40"><path d="M0 0H347V24H145L130 36L115 24H0Z" fill="#2e3192"/></svg>
    </div>
    <div class="copy">
      <h2>Life Coaching</h2>
      <h5>Relationships</h5>
      <p>Lorem Ipsum is simply dummy text of the printing and typesetting industry. Lorem Ipsum has been the industry's standard dummy text ever since the 1500s, when an unknown printer took a galley of type and scrambled it to make a type specimen book. It has survived not only five centuries, but also the leap into electronic typesetting, remaining essentially unchanged. It was popularised in the 1960s with the release of Letraset sheets containing Lorem Ipsum passages, and more recently with desktop publishing software like Aldus PageMaker including versions of Lorem Ipsum.</p>
      <hr>
    </div>
  </div>

  <div class="panel purpose">
    <div class="copy">
      <h5>Life Purpose</h5>
      <p>Lorem Ipsum is simply dummy text of the printing and typesetting industry. Lorem Ipsum has been the industry's standard dummy text ever since the 1500s, when an unknown printer took a galley of type and scrambled it to make a type specimen book. It has survived not only five centuries, but also the leap into electronic typesetting.</p>
      <h5>Confidence</h5>
      <p>Lorem Ipsum is simply dummy text of the printing and typesetting industry. Lorem Ipsum has been the industry's standard dummy text ever since the 1500s, when an unknown printer took a galley of type and scrambled it to make a type specimen book. It has survived not only five centuries, but also the leap into electronic typesetting.</p>
      <h5>Overwhelm/Health</h5>
      <p>Lorem Ipsum is simply dummy text of the printing and typesetting industry. Lorem Ipsum has been the industry's standard dummy text ever since the 1500s, when an unknown printer took a galley of type and scrambled it to make a type specimen book. It has survived not only five centuries, but also the leap into electronic typesetting.</p>
    </div>
    <div class="darkband"></div>
    <svg style="position:absolute;left:0;top:345px" width="347" height="12" viewBox="0 0 347 12"><path d="M160 0L173 11L186 0Z" fill="#5a5a5a"/></svg>
    <div class="scene" role="img" aria-label="Photo of a smiling woman resting on an exercise mat with a water bottle and dumbbells"></div>
  </div>

  <div class="panel wellness">
    <div class="scene" role="img" aria-label="Photo of a natural spring pool beneath a limestone grotto with trees"></div>
    <div class="notchband" style="top:236px">
      <svg width="347" height="40" viewBox="0 0 347 40"><path d="M0 0H347V18H150L138 30L126 18H0Z" fill="#1e9a4a"/></svg>
    </div>
    <div class="copy">
      <h2>Wellness Coaching</h2>
      <h5>Weight Loss</h5>
      <p>Lorem Ipsum is simply dummy text of the printing and typesetting industry. Lorem Ipsum has been the industry's standard dummy text ever since the 1500s, when an unknown printer took a galley of type and scrambled it to make a type specimen book. It has survived not only five centuries, but also the leap into electronic typesetting.</p>
      <hr>
      <h5>Energy, Fitness.</h5>
      <p>Lorem Ipsum is simply dummy text of the printing and typesetting industry. Lorem Ipsum has been the industry's standard dummy text ever since the 1500s, when an unknown printer took a galley of type and scrambled it to make a type specimen book. It has survived not only five centuries, but also the leap into electronic typesetting.</p>
    </div>
  </div>
</section>

</body>
</html>
```